依頼詳細
https://www.hikarinova-ex.jp/pr/1/
こちらのLPサイトへ誘導バナーです。
現在、同時に制作中の為PC用のサイトしか用意しておりません。後日、スマホ用のサイトも完成予定です。
サイズは
横 240 × 縦 120 (表示 120 × 60)
横 936 × 縦 120 (表示 468 × 60)
横 468 × 縦 120 (表示 234 × 60)
横 600 × 縦 500 (表示 300 × 250)
横 200 × 縦 120 (表示 100 × 60)
横 640 × 縦 100 (表示 320 × 50)
横250 × 縦 250 (表示 125 × 125)
横200 × 縦 200 (表示 100 × 100)
容量制限
200KB 以下
ファイル形式:
JPG / PNG /
記載項目
電気まだ変えてないの?
サイト名:光ノバケアネット
特に細かく決めていないので、よいキャッチなどがありましたら作成して頂ければと思います。
サイズ
• 250 x 250 ( スクエアポップアップ )
• 200 x 200 ( スクエア )
• 240×120/936×120/468×120/600×500/200×120/640×100
希望イメージ
シンプル 複雑
単色 カラフル
暗い 明るい
日常 高級
遊び心 厳粛
未来的 伝統的
女性的 男性的
希望する色
黄・オレンジ系、緑系、水色系
納品ファイル
• 高解像度JPG (.jpg)
• PNG形式 (.png)
補足説明
■ 選んだ理由

修正にも素早いご対応をして頂きました。
バナーのデザインをお願いしたのですが、シンプルで程よい文字数だった為
選ばせて頂きました。

■ 提案者全員のお礼・コメント

今回、素早い対応をして頂きありがとうございました。
また、次回お願いすることもあると思いますので
その際は、よろしくお願いいたします。

```html
<!DOCTYPE html>
<html lang="ja">
<head>
<meta charset="utf-8">
<title>光ノバケアネット バナー案</title>
<link rel="stylesheet" href="https://fonts.googleapis.com/css2?family=M+PLUS+Rounded+1c:wght@800&family=Noto+Sans+JP:wght@400;500&display=swap">
<style>
  :root{
    --sheet:#f2f2f2;
    --ink:#222;
    --teal:#1fa48b;
    --yellow:#ffec1f;
    --brand:#2f9e3c;
    --orange:#f0602a;
    --white:#ffffff;
    --photo-a:#d9d4cf;
    --photo-b:#8d8f94;
  }
  *{box-sizing:border-box;margin:0;padding:0}
  html,body{width:781px;height:1200px;overflow:hidden;background:var(--sheet)}
  body{position:relative;font-family:"Noto Sans JP",sans-serif;color:var(--ink)}
  .sheet-title{position:absolute;left:12px;top:18px;font-size:36px;font-weight:400;letter-spacing:1px}
  .size-label{position:absolute;font-size:21px;font-weight:400}
  .banner{position:absolute;background:var(--teal);overflow:hidden;border:1px solid #bdbdbd}
  .photo{position:absolute;background:linear-gradient(180deg,var(--photo-a),var(--photo-b))}
  .catch{position:absolute;text-align:center;color:var(--white);font-family:"M PLUS Rounded 1c",sans-serif;font-weight:800;line-height:1.15;text-shadow:0 1px 2px rgba(0,0,0,.25)}
  .catch span{display:block}
  .catch-key{color:var(--yellow);font-size:1.55em;line-height:1.1}
  .catch-key svg{width:.6em;height:.75em;vertical-align:-.05em;margin-left:.05em}
  .catch-ask{font-size:1.12em}
  .brand-box{position:absolute;background:var(--white);color:var(--brand);font-weight:500;text-align:center;line-height:1.1;letter-spacing:.06em}
  .brand-tag{display:block;color:var(--ink);font-weight:400;letter-spacing:0}
  .cta{position:absolute;background:var(--orange);color:var(--white);display:flex;align-items:center;justify-content:center;white-space:nowrap}
  .cta-easy{display:inline-block;font-size:.5em;line-height:1;width:1em;margin-right:.25em;text-align:center}
  .slant{clip-path:polygon(7% 0,100% 0,100% 100%,0 100%)}
  .corner{position:absolute;right:0;top:0;background:var(--orange);color:var(--white);text-align:right;line-height:1.1;clip-path:polygon(0 0,100% 0,100% 100%)}
  .corner span{position:absolute;right:3px;top:2px}
</style>
</head>
<body>
<svg width="0" height="0" style="position:absolute">
  <defs>
    <symbol id="bulb" viewBox="0 0 20 26">
      <circle cx="10" cy="10" r="9" fill="#ffd21f" stroke="#e0a800" stroke-width="1"/>
      <rect x="6" y="18" width="8" height="6" rx="1.5" fill="#b9b9b9"/>
    </symbol>
  </defs>
</svg>

<h1 class="sheet-title">「光ノバケアネット」　バナー案</h1>

<!-- 600x500 -->
<p class="size-label" style="left:29px;top:82px">600×500</p>
<div class="banner" style="left:30px;top:121px;width:459px;height:382px">
  <div class="photo" role="img" aria-label="スーツ姿で指を立てる女性の写真" style="left:287px;top:27px;width:172px;height:308px"></div>
  <div class="catch" style="left:0;top:56px;width:300px;font-size:30px">
    <span>あなたの会社の</span>
    <span class="catch-key">電気<svg><use href="#bulb"/></svg></span>
    <span class="catch-ask">まだ変えないの?</span>
  </div>
  <div class="brand-box" style="left:0;top:335px;width:230px;height:47px;font-size:24px;padding-top:5px">光ノバケアネット<span class="brand-tag" style="font-size:8px;margin-top:2px">グリーン電力をもっと使いやすく</span></div>
  <div class="cta slant" style="left:208px;top:335px;width:251px;height:47px;font-size:28px"><span class="cta-easy">簡単</span>5分でお見積もり</div>
</div>

<!-- 250x250 -->
<p class="size-label" style="left:551px;top:82px">250 x 250</p>
<div class="banner" style="left:550px;top:124px;width:192px;height:192px">
  <div class="brand-box" style="left:0;top:0;width:192px;height:37px;font-size:20px;padding-top:6px">光ノバケアネット</div>
  <div class="photo" role="img" aria-label="スーツ姿で指を立てる女性の写真" style="left:134px;top:52px;width:58px;height:102px"></div>
  <div class="catch" style="left:0;top:52px;width:136px;font-size:14px">
    <span>あなたの会社の</span>
    <span class="catch-key">電気<svg><use href="#bulb"/></svg></span>
    <span class="catch-ask">まだ変えないの?</span>
  </div>
  <div class="cta" style="left:0;top:154px;width:192px;height:38px;font-size:20px"><span class="cta-easy">簡単</span>5分でお見積もり</div>
</div>

<!-- 200x200 -->
<p class="size-label" style="left:551px;top:365px">200 x 200</p>
<div class="banner" style="left:551px;top:403px;width:153px;height:153px">
  <div class="brand-box" style="left:0;top:0;width:153px;height:28px;font-size:16px;padding-top:4px">光ノバケアネット</div>
  <div class="catch" style="left:0;top:32px;width:153px;font-size:15px">
    <span>あなたの会社の</span>
    <span class="catch-key">電気<svg><use href="#bulb"/></svg></span>
    <span class="catch-ask">まだ変えないの?</span>
  </div>
  <div class="cta" style="left:0;top:123px;width:153px;height:30px;font-size:17px"><span class="cta-easy">簡単</span>5分でお見積もり</div>
</div>

<!-- 240x120 -->
<p class="size-label" style="left:28px;top:568px">240×120</p>
<div class="banner" style="left:28px;top:608px;width:184px;height:91px">
  <div class="photo" role="img" aria-label="スーツ姿で指を立てる女性の写真" style="left:109px;top:14px;width:42px;height:59px"></div>
  <div class="corner" style="width:75px;height:60px;font-size:10px"><span>見積もり<br>簡単<br>5分</span></div>
  <div class="catch" style="left:0;top:8px;width:108px;font-size:11px">
    <span>あなたの会社の</span>
    <span class="catch-key">電気<svg><use href="#bulb"/></svg></span>
    <span class="catch-ask">まだ変えないの?</span>
  </div>
  <div class="brand-box" style="left:0;top:73px;width:184px;height:18px;font-size:13px;padding-top:1px">光ノバケアネット</div>
</div>

<!-- 200x120 -->
<p class="size-label" style="left:283px;top:554px">200×120</p>
<div class="banner" style="left:289px;top:605px;width:152px;height:91px">
  <div class="corner" style="width:60px;height:50px;font-size:10px"><span>見積もり<br>5分</span></div>
  <div class="catch" style="left:0;top:8px;width:120px;font-size:11px">
    <span>あなたの会社の</span>
    <span class="catch-key">電気<svg><use href="#bulb"/></svg></span>
    <span class="catch-ask">まだ変えないの?</span>
  </div>
  <div class="brand-box" style="left:0;top:73px;width:152px;height:18px;font-size:13px;padding-top:1px">光ノバケアネット</div>
</div>

<!-- 468x120 -->
<p class="size-label" style="left:30px;top:724px">468×120</p>
<div class="banner" style="left:34px;top:769px;width:358px;height:92px">
  <div class="photo" role="img" aria-label="スーツ姿で指を立てる女性の写真" style="left:142px;top:4px;width:58px;height:88px"></div>
  <div class="catch" style="left:0;top:8px;width:140px;font-size:13px">
    <span>あなたの会社の</span>
    <span class="catch-key">電気<svg><use href="#bulb"/></svg></span>
    <span class="catch-ask">まだ変えないの?</span>
  </div>
  <div class="brand-box" style="left:243px;top:0;width:115px;height:61px;font-size:19px;padding-top:7px;text-align:left;padding-left:9px">光ノバ<br>ケアネット</div>
  <div class="cta slant" style="left:199px;top:61px;width:159px;height:31px;font-size:17px"><span class="cta-easy">簡単</span>5分でお見積もり</div>
</div>

<!-- 640x100 -->
<p class="size-label" style="left:41px;top:877px">640×100</p>
<div class="banner" style="left:27px;top:930px;width:490px;height:76px">
  <div class="photo" role="img" aria-label="スーツ姿で指を立てる女性の写真" style="left:187px;top:4px;width:50px;height:72px"></div>
  <div class="catch" style="left:40px;top:5px;width:146px;font-size:13px">
    <span>あなたの会社の</span>
    <span class="catch-key">電気<svg><use href="#bulb"/></svg></span>
    <span class="catch-ask">まだ変えないの?</span>
  </div>
  <div class="brand-box" style="left:308px;top:0;width:182px;height:76px;font-size:19px;padding-top:7px">光ノバケアネット<span class="brand-tag" style="font-size:7px;margin-top:1px">グリーン電力をもっと使いやすく</span></div>
  <div class="cta slant" style="left:325px;top:47px;width:165px;height:29px;font-size:17px"><span class="cta-easy">簡単</span>5分でお見積もり</div>
</div>

<!-- 936x120 -->
<p class="size-label" style="left:41px;top:1037px">936×120</p>
<div class="banner" style="left:27px;top:1080px;width:716px;height:92px">
  <div class="photo" role="img" aria-label="スーツ姿で指を立てる女性の写真" style="left:286px;top:4px;width:62px;height:88px"></div>
  <div class="catch" style="left:106px;top:7px;width:170px;font-size:16px">
    <span>あなたの会社の</span>
    <span class="catch-key">電気<svg><use href="#bulb"/></svg></span>
    <span class="catch-ask">まだ変えないの?</span>
  </div>
  <div class="brand-box" style="left:461px;top:0;width:255px;height:92px;font-size:27px;padding-top:5px">光ノバケアネット<span class="brand-tag" style="font-size:8px;margin-top:1px">グリーン電力をもっと使いやすく</span></div>
  <div class="cta slant" style="left:511px;top:53px;width:205px;height:39px;font-size:22px"><span class="cta-easy">簡単</span>5分でお見積もり</div>
</div>
</body>
</html>
```